FB and Youtube banner design for HVAC company

I would like an appealing site page banner for business page on Facebook (851w x 315h pixels) and one for youtube (2560w x 1440h pixels) for hvac company. Business card design and logo are attached. Company name is Bright Meadow Air Conditioning, Refrigeration, and Heating.

NOTE: I put the business cards and log up to see some of the artwork the company is using. It's not to replicate that in the banner images.

Target Market(s)

Interested business and homeowner visitors to Facebook business page and youtube channel page.

Industry/Entity Type

Hvac

Font styles to use
Sans Serif

Requirements
Must have
• See logo for color scheme.
Should not have
• This should not look like a business card. Think of what is typically the banner on a facebook business page and youtube channel.

```html
<!DOCTYPE html>
<html lang="en">
<head>
<meta charset="utf-8">
<title>Bright Meadow – Social Banners</title>
<link rel="stylesheet" href="https://fonts.googleapis.com/css2?family=Archivo:wght@800&family=Michroma&family=Montserrat:wght@400&family=Roboto+Condensed:wght@700&family=Roboto:wght@700&display=swap">
<style>
  :root{
    --board:#ececed;
    --navy:#0b2455;
    --orange:#ff6600;
    --blue:#0a48c6;
    --charcoal:#4d4d4d;
    --white:#ffffff;
    --panel:#e4e5e8;
    --panel-edge:#c9cacd;
    --label:#9a9a9a;
  }
  html,body{margin:0;padding:0;overflow:hidden;}
  body{width:1200px;height:1200px;background:var(--board);}
  .board{display:block;width:1200px;height:1200px;}
  .navy{fill:var(--navy);}
  .orange{fill:var(--orange);}
  .blue{fill:var(--blue);}
  .white{fill:var(--white);}
  .panel{fill:var(--panel);}
  .panel-edge{fill:var(--panel-edge);}
  .rule{fill:none;stroke:var(--navy);}
  .lead{fill:none;stroke:var(--orange);stroke-width:1.5;}
  .size-label{font-family:"Montserrat",sans-serif;font-size:32px;fill:var(--label);}
  .palette-label{font-family:"Montserrat",sans-serif;font-size:22px;fill:#333;letter-spacing:.5px;}
  .call{font-family:"Michroma",sans-serif;fill:var(--navy);}
  .phone{font-family:"Roboto",sans-serif;font-weight:700;fill:var(--white);}
  .contact{font-family:"Roboto Condensed",sans-serif;font-weight:700;fill:var(--white);}
  .brand{font-family:"Archivo",sans-serif;font-weight:800;}
  .service{font-family:"Michroma",sans-serif;fill:var(--navy);}
  .web{font-family:"Roboto Condensed",sans-serif;font-weight:700;fill:var(--orange);}
</style>
</head>
<body>
<svg class="board" viewBox="0 0 1200 1200" xmlns="http://www.w3.org/2000/svg">
  <defs>
    <linearGradient id="board-bg" x1="0" y1="0" x2="1" y2="1">
      <stop offset="0" stop-color="#f4f4f5"/>
      <stop offset="1" stop-color="#e2e2e4"/>
    </linearGradient>
    <linearGradient id="worksite" x1="0" y1="0" x2="1" y2="1">
      <stop offset="0" stop-color="#8d8f95"/>
      <stop offset=".45" stop-color="#a3a4a8"/>
      <stop offset=".75" stop-color="#8a6f6a"/>
      <stop offset="1" stop-color="#9c8f55"/>
    </linearGradient>
  </defs>

  <rect width="1200" height="1200" fill="url(#board-bg)"/>

  <!-- Page banner (851x315) -->
  <g class="page-banner-label">
    <rect x="117" y="43" width="58" height="58" rx="6" class="blue"/>
    <text x="182" y="85" class="size-label">851x315 px</text>
  </g>

  <g class="page-banner">
    <g role="img" aria-label="Blurred photo of an HVAC technician at work">
      <rect x="117" y="111" width="953" height="353" fill="url(#worksite)"/>
    </g>
    <rect class="contact-frame" x="170" y="174" width="330" height="224" fill="#ffffff" fill-opacity=".18" stroke="var(--charcoal)" stroke-width="5"/>
    <polygon class="orange" points="456,111 468,111 672,464 608,464"/>
    <polygon class="white" points="468,111 480,111 696,464 672,464"/>
    <polygon class="navy" points="480,111 584,111 768,464 696,464"/>
    <polygon class="panel-edge" points="584,111 1070,111 1070,464 768,464"/>
    <polygon class="panel" points="596,119 1062,119 1062,456 774,456"/>
    <polygon class="panel-edge" points="1062,176 1038,208 1062,240"/>

    <text x="330" y="243" text-anchor="middle" class="call" font-size="19" letter-spacing="3">CALL US NOW</text>
    <rect x="212" y="248" width="234" height="38" rx="5" class="blue"/>
    <text x="329" y="279" text-anchor="middle" class="phone" font-size="30" letter-spacing="1">555.214.0188</text>

    <g class="icon-web" fill="none" stroke="#fff" stroke-width="1.6">
      <circle cx="225" cy="310" r="10"/>
      <ellipse cx="225" cy="310" rx="4.5" ry="10"/>
      <line x1="215" y1="310" x2="235" y2="310"/>
    </g>
    <text x="243" y="317" class="contact" font-size="21">www.meadowhvac.com</text>
    <g class="icon-mail" fill="none" stroke="#fff" stroke-width="1.6">
      <rect x="214" y="334" width="23" height="15"/>
      <polyline points="214,334 225.5,343 237,334"/>
    </g>
    <text x="243" y="349" class="contact" font-size="19">dana@meadowhvac.com</text>

    <circle cx="720" cy="208" r="40" fill="none" stroke="var(--orange)" stroke-width="4"/>
    <text x="776" y="203" class="brand blue" font-size="46">BRIGHT</text>
    <text x="776" y="256" class="brand blue" font-size="46">MEADOW</text>

    <path class="rule" stroke-width="2.5" d="M678,291 H1018 V324 H700"/>
    <text x="1004" y="316" text-anchor="end" class="service" font-size="15" letter-spacing="1.5">AIR CONDITIONING</text>
    <path class="rule" stroke-width="2.5" d="M700,334 H1062 M790,334 V367 H1062"/>
    <text x="986" y="359" text-anchor="end" class="service" font-size="15" letter-spacing="1.5">REFRIGERATION</text>
    <path class="rule" stroke-width="2.5" d="M836,377 H956 V409 H736"/>
    <text x="946" y="401" text-anchor="end" class="service" font-size="15" letter-spacing="1.5">HEATING</text>
  </g>

  <!-- Palette -->
  <g class="palette">
    <text x="688" y="546" class="palette-label">COLORS USED</text>
    <rect x="874" y="522" width="32" height="32" rx="6" fill="var(--white)"/>
    <rect x="913" y="522" width="32" height="32" rx="6" fill="var(--charcoal)"/>
    <rect x="952" y="522" width="32" height="32" rx="6" fill="var(--orange)"/>
    <rect x="990" y="522" width="32" height="32" rx="6" fill="var(--blue)"/>
    <rect x="1030" y="522" width="32" height="32" rx="6" fill="var(--navy)"/>
  </g>

  <!-- Channel banner (2560x1440) -->
  <g class="channel-banner-label">
    <rect x="114" y="544" width="58" height="58" rx="6" fill="#d8312a"/>
    <text x="182" y="586" class="size-label">2560x1440 px</text>
  </g>

  <g class="channel-banner">
    <rect x="114" y="613" width="953" height="534" class="orange"/>
    <polygon class="white" points="408,613 414,613 744,1147 728,1147"/>
    <polygon class="navy" points="414,613 1067,613 1067,1147 744,1147"/>

    <g role="img" aria-label="Blurred photo of an HVAC technician at work">
      <polygon points="114,802 520,802 586,958 114,958" fill="url(#worksite)"/>
    </g>
    <rect class="contact-frame" x="327" y="821" width="204" height="109" fill="#ffffff" fill-opacity=".18" stroke="var(--charcoal)" stroke-width="3"/>
    <text x="424" y="852" text-anchor="middle" class="call" font-size="11" letter-spacing="2">CALL US NOW</text>
    <rect x="358" y="854" width="131" height="22" rx="3" class="blue"/>
    <text x="423" y="872" text-anchor="middle" class="phone" font-size="17">555.214.0188</text>
    <g fill="none" stroke="#fff" stroke-width="1">
      <circle cx="366" cy="888" r="6"/>
      <ellipse cx="366" cy="888" rx="2.6" ry="6"/>
      <line x1="360" y1="888" x2="372" y2="888"/>
    </g>
    <text x="375" y="892" class="contact" font-size="12">www.meadowhvac.com</text>
    <g fill="none" stroke="#fff" stroke-width="1">
      <rect x="360" y="902" width="13" height="8"/>
      <polyline points="360,902 366.5,907 373,902"/>
    </g>
    <text x="375" y="910" class="contact" font-size="11">dana@meadowhvac.com</text>

    <circle cx="201" cy="704" r="27" fill="none" stroke="var(--navy)" stroke-width="3"/>
    <text x="238" y="702" class="brand navy" font-size="29">BRIGHT</text>
    <text x="238" y="733" class="brand navy" font-size="29">MEADOW</text>
    <text x="275" y="746" text-anchor="middle" class="service" font-size="6.4" letter-spacing=".6">AIR CONDITIONING · REFRIGERATION · HEATING</text>

    <polygon class="panel" points="578,802 1056,802 1056,958 658,958"/>
    <rect x="1056" y="802" width="11" height="156" class="panel-edge"/>
    <polygon class="panel-edge" points="1056,864 1044,880 1056,896"/>

    <circle cx="692" cy="846" r="22" fill="none" stroke="var(--orange)" stroke-width="2.5"/>
    <text x="724" y="843" class="brand blue" font-size="24">BRIGHT</text>
    <text x="724" y="870" class="brand blue" font-size="24">MEADOW</text>

    <path class="rule" stroke-width="1.5" d="M620,882 H814 V898 H632"/>
    <text x="808" y="894" text-anchor="end" class="service" font-size="8.5" letter-spacing=".8">AIR CONDITIONING</text>
    <path class="rule" stroke-width="1.5" d="M704,904 H982 V1094 M704,904 V919 H967 V1094 M640,919 H704"/>
    <text x="710" y="916" class="service" font-size="8.5" letter-spacing=".8">REFRIGERATION</text>
    <path class="rule" stroke-width="1.5" d="M786,924 V940 H660 M728,924 H786"/>
    <text x="780" y="936" text-anchor="end" class="service" font-size="8.5" letter-spacing=".8">HEATING</text>
    <path class="lead" d="M982,962 V1094 M967,922 V1094"/>

    <rect x="766" y="1094" width="254" height="31" fill="none" stroke="var(--orange)" stroke-width="1.5"/>
    <text x="893" y="1118" text-anchor="middle" class="web" font-size="23">www.meadowhvac.com</text>
  </g>
</svg>
</body>
</html>
```